The Quiet Tide of Morning: A Path Through Silence, Courage and Light

I require designs for the front cover, rear cover and spine for a printed book. The book is the personal account of a stroke survivor.

Dimensions requested by publisher:|

Front + rear covers = 130 x 195mm with 3-5mm bleed
Spine = c. 10mm

Target Market(s)

Worldwide

Font styles to use
Decorative
Script

Requirements
Must have
• The text for the back cover (and I have attached photos for the accompanying headshot):

"Ruth Kembo had become a successful commercial lawyer in Tanzania with a professional career that spanned almost two decades. One week after celebrating her law firm’s 5th anniversary her life changed dramatically when at 4am one morning she suffered an ischaemic stroke.

After losing the use of the right side of her body and her ability to speak and swallow, Ruth was forced to undergo a full system reboot. In this brutally honest account of her life before and after the stroke Ruth describes her physical and mental battles, how she managed to accept the condition and deal with the accompanying feelings of shame.

Her story is one of rebirth, hope and ultimately transformation, offering practical advice for stroke survivors, their families and anyone embarking on a rehabilitation programme following serious illness."
Nice to have
• Modern but elegant feel. Something that signifies the metamorphosis of a butterfly, or transformation in general.

```html
<!DOCTYPE html>
<html lang="en">
<head>
<meta charset="utf-8">
<title>The Quiet Tide of Morning — Cover Spread</title>
<link href="https://fonts.googleapis.com/css2?family=Kaushan+Script&family=Montserrat:wght@400;500&family=Lato:wght@400&family=Ubuntu:wght@700&display=swap" rel="stylesheet">
<style>
  :root {
    --paper: #f7f8f8;
    --plum: #9a72a0;
    --plum-deep: #8d6497;
    --ink: #1e1e1e;
    --slate: #6e6e6e;
    --white: #ffffff;
  }
  * { margin: 0; padding: 0; box-sizing: border-box; }
  html, body { width: 1200px; height: 853px; overflow: hidden; background: var(--paper); }
  .spread { position: relative; width: 1200px; height: 853px; background: var(--paper); overflow: hidden; }

  /* Back cover */
  .author-portrait {
    position: absolute; left: 0; top: 30px; width: 295px; height: 740px;
    background:
      linear-gradient(90deg, rgba(247,248,248,0) 72%, var(--paper) 100%),
      linear-gradient(180deg, rgba(247,248,248,0) 0%, #c7adcb 20%, #a880ad 55%, #b393b8 85%, #d8c9da 100%);
  }
  .back-blurb {
    position: absolute; right: 653px; top: 48px; width: 322px;
    font-family: "Lato", sans-serif; font-size: 17.6px; line-height: 22px;
    color: var(--ink); text-align: right;
  }
  .back-blurb p { margin-left: auto; }
  .back-blurb p + p { margin-top: 22px; }
  .back-blurb .para-intro { width: 322px; }
  .back-blurb .para-story { width: 272px; }
  .back-blurb .para-close { width: 282px; }

  /* Spine */
  .spine-title {
    position: absolute; left: 600px; top: 88px;
    transform-origin: 0 0; transform: rotate(90deg) translateY(-50%);
    white-space: nowrap; color: var(--plum-deep);
    display: flex; align-items: center; gap: 16px;
  }
  .spine-title .caps { font-family: "Montserrat", sans-serif; font-size: 17px; letter-spacing: 11px; }
  .spine-title .script { font-family: "Kaushan Script", cursive; font-size: 52px; line-height: 1; }

  /* Front cover */
  .front-title { position: absolute; left: 668px; top: 0; width: 520px; height: 380px; color: var(--plum-deep); z-index: 2; font-weight: 400; }
  .front-title span { position: absolute; left: 0; white-space: nowrap; line-height: 1; }
  .front-title .caps { font-family: "Montserrat", sans-serif; font-weight: 500; font-size: 50px; letter-spacing: 27px; }
  .front-title .script { font-family: "Kaushan Script", cursive; font-size: 96px; }
  .front-title .line-1 { top: 56px; }
  .front-title .line-2 { top: 112px; }
  .front-title .line-3 { top: 216px; }
  .front-title .line-4 { top: 254px; }

  .subtitle {
    position: absolute; left: 670px; top: 385px;
    font-family: "Ubuntu", sans-serif; font-weight: 700;
    font-size: 46px; line-height: 50px; color: var(--slate);
  }
  .subtitle span { display: block; }

  .butterfly-figure {
    position: absolute; left: 885px; top: 390px; width: 310px; height: 380px; z-index: 1;
    background: radial-gradient(ellipse at 55% 50%, #b592bb 0%, #d7c5da 55%, rgba(247,248,248,0) 75%);
  }

  .author-band {
    position: absolute; left: 0; bottom: 0; width: 1200px; height: 83px;
    background: var(--plum); z-index: 3;
  }
  .author-name {
    position: absolute; left: 702px; top: 790px; z-index: 4;
    font-family: "Montserrat", sans-serif; font-size: 33px; letter-spacing: 18px;
    color: var(--white); line-height: 1; white-space: nowrap;
  }
</style>
</head>
<body>
<main class="spread">
  <section class="back-cover">
    <div class="author-portrait" role="img" aria-label="Portrait photograph of the author in a lilac trouser suit"></div>
    <div class="back-blurb">
      <p class="para-intro">Ruth Kembo had become a successful commercial lawyer in Tanzania with a professional career that spanned almost two decades. One week after celebrating her law firm’s 5th anniversary her life changed dramatically when at 4am one morning she suffered an ischaemic stroke.</p>
      <p class="para-story">After losing the use of the right side of her body and her ability to speak and swallow, Ruth was forced to undergo a full system reboot. In this brutally honest account of her life before and after the stroke Ruth describes her physical and mental battles, how she managed to accept the condition and deal with the accompanying feelings of shame.</p>
      <p class="para-close">Her story is one of rebirth, hope and ultimately transformation, offering practical advice for stroke survivors, their families and anyone embarking on a rehabilitation programme following serious illness.</p>
    </div>
  </section>

  <div class="spine-title">
    <span class="caps">THE</span>
    <span class="script">Quiet Tide</span>
    <span class="caps">OF</span>
    <span class="script">Morning</span>
  </div>

  <section class="front-cover">
    <h1 class="front-title">
      <span class="caps line-1">THE</span>
      <span class="script line-2">Quiet Tide</span>
      <span class="caps line-3">OF</span>
      <span class="script line-4">Morning</span>
    </h1>
    <p class="subtitle">
      <span>A</span>
      <span>Path</span>
      <span>Through</span>
      <span>Silence,</span>
      <span>Courage</span>
      <span>and Light</span>
    </p>
    <div class="butterfly-figure" role="img" aria-label="Illustration of a kneeling figure with large butterfly wings, in lilac line art"></div>
  </section>

  <div class="author-band"></div>
  <p class="author-name">RUTH KEMBO</p>
</main>
</body>
</html>
```